bRevik Equity Advisors Website

We are interested in developing a complete website and long term maintenance with the developer we choose through this contest.

Brevik is a financial consulting company. We will have a website that capitalizes on the initial costs of retaining a client by providing additional services the client needs and tyically spend using 3rd parties.

The primary function of the website will be structured as a sales tool to retain and provide financial services to the client. Also, to provide other services that are integral to starting, building, and growing a business in order to increase creditibility and maintain client loyalty.

Through a combination of in-house "white label" services as well well chosen outside professional services as "affiliates".

The website home page must be a an instant curb-side appeal and representation of our desired extraordinary image. That image is a robust, innovative (bRevik), with a sophistication that creates an instant emotion of excitement and confidence that they have finally found that "needle in the haystack" they have been seeking. The feeling that they are compelled to take action lest they lose our contact information and are doomed to sink to the mediocrity that most business accept through a lack of effort and forsite.

Reason: Emails were going to the wrong account and I didn't receive any notices of questions or designs being posted.

Target Market(s)

Startup, growth and advancing companies seeking capital and other business services such as website and corporate image design, legal, marketing, asset management, investment and business consulting, etc.

Industry/Entity Type

Financial

Requirements
Must have
• We want to see your creativity
Nice to have
Should not have

```html
<!DOCTYPE html>
<html lang="en">
<head>
<meta charset="utf-8">
<title>bRevik Equity Advisors</title>
<link href="https://fonts.googleapis.com/css2?family=Ubuntu:wght@300;400;500&family=PT+Sans:wght@400;700&family=Noto+Serif&family=Roboto+Condensed:wght@700&display=swap" rel="stylesheet">
<style>
:root{
  --bg:#030a17;
  --bg-deep:#01050d;
  --blue:#1765b8;
  --blue-dark:#0a3c80;
  --blue-light:#3e95e0;
  --teal:#1fb0d8;
  --teal-panel:#16a9cc;
  --cyan-text:#27b5e0;
  --yellow:#f5c51a;
  --yellow-dark:#c99a08;
  --white:#ffffff;
  --muted:#c9d4e0;
  --grey:#7f8c9a;
}
*{margin:0;padding:0;box-sizing:border-box}
html,body{width:1200px;height:1178px;overflow:hidden;background:var(--bg)}
body{position:relative;font-family:"PT Sans",sans-serif;color:var(--white)}
.backdrop{position:absolute;left:0;top:0;width:1200px;height:520px;
  background:
    repeating-linear-gradient(90deg,rgba(30,110,200,0) 0 38px,rgba(40,130,220,.18) 46px,rgba(30,110,200,0) 60px 92px),
    radial-gradient(ellipse 60% 100% at 58% 0%,#0d4a9a 0%,#062a5c 35%,rgba(3,10,23,0) 80%);
  -webkit-mask:linear-gradient(#000 0%,#000 30%,transparent 100%);mask:linear-gradient(#000 0%,#000 30%,transparent 100%)}
.abs{position:absolute}

.brand{left:43px;top:20px;display:flex;align-items:center;gap:10px}
.brand-mark{width:18px;height:40px;background:var(--yellow)}
.brand-name{font-family:"Ubuntu",sans-serif;font-weight:400;font-size:46px;letter-spacing:4px;color:var(--blue-light);line-height:1}
.tagline{left:43px;top:82px;font-family:"Ubuntu",sans-serif;font-size:15px;color:var(--white)}

.account{left:932px;top:94px;width:242px;height:40px;
  background:linear-gradient(#2a7fd6,#0b4a9a);clip-path:polygon(14px 0,100% 0,100% 100%,0 100%);
  display:flex;align-items:center;justify-content:center;gap:14px;font-family:"Ubuntu",sans-serif;font-weight:500;font-size:14px}

.nav{left:24px;top:134px;width:1150px;height:48px;
  background:linear-gradient(#2c82d8 0%,#1460b4 50%,#0c4894 100%);
  clip-path:polygon(0 0,100% 0,97.5% 100%,2.5% 100%);display:flex;align-items:center;padding-left:24px}
.nav a{font-family:"Ubuntu",sans-serif;font-size:18px;color:var(--white);text-decoration:none;height:48px;line-height:48px;padding:0 22px;border-right:1px solid rgba(0,30,80,.5);box-shadow:1px 0 0 rgba(120,180,240,.25)}
.search{left:798px;top:146px;width:302px;height:24px;background:var(--white);border:1px solid #0a3c80}
.search-btn{left:1103px;top:146px;width:54px;height:24px;background:var(--yellow);clip-path:polygon(0 0,100% 0,88% 100%,0 100%)}

.services{left:50px;top:204px;width:267px;height:232px;background:linear-gradient(#1fb8d8,#0e9ec4)}
.services ul{list-style:none;position:absolute;left:22px;top:16px;width:230px}
.services li{font-family:"Ubuntu",sans-serif;font-size:17px;height:36px;line-height:32px;border-bottom:1px solid rgba(255,255,255,.22);padding-left:22px;position:relative}
.services li::before{content:"";position:absolute;left:4px;top:12px;width:7px;height:7px;border:1px solid var(--white);transform:rotate(45deg)}
.services-tab{left:24px;top:219px;width:40px;height:194px;background:linear-gradient(90deg,var(--yellow-dark),var(--yellow) 40%);clip-path:polygon(0 8%,100% 0,100% 100%,0 94%)}
.services-tab span{position:absolute;left:4px;top:97px;transform:translate(0,-50%) rotate(-90deg);transform-origin:center;width:140px;margin-left:-52px;text-align:center;font-family:"Ubuntu",sans-serif;font-size:16px;color:#2a2200;letter-spacing:1px}

.hero{left:323px;top:204px;width:829px;height:232px;background:#0e5aa8;padding:5px}
.hero-photo{width:100%;height:100%;background:linear-gradient(100deg,#2a4f9a 0%,#7ba4d0 35%,#c6d8ea 60%,#8fb0cc 100%)}
.hero-caption{position:absolute;left:5px;right:5px;bottom:5px;height:44px;background:rgba(20,30,50,.55)}
.dots{left:344px;top:408px;display:flex;gap:4px}
.dots i{width:12px;height:12px;border-radius:50%;background:var(--yellow);display:block}
.dots i.on{background:#d8dde6}

.welcome{left:50px;top:458px;font-family:"Ubuntu",sans-serif;font-weight:300;font-size:29px;color:var(--yellow);white-space:nowrap}
.welcome em{font-style:normal;font-size:42px;color:var(--cyan-text)}
.rule{height:0;border-top:1px dashed #1b6e8c}

.intro-lead{left:50px;top:542px;width:630px;font-size:17px;line-height:21px;color:var(--cyan-text)}
.body-copy{font-size:12.6px;line-height:21.5px;color:var(--white)}
.read-more{left:50px;top:710px;font-size:12.5px;color:var(--yellow)}
.read-more::after{content:" ······›";color:var(--yellow)}
.intro-photo{left:703px;top:545px;width:448px;height:186px;border:1px solid #7a8796;background:linear-gradient(90deg,#dfe6ee 0%,#f4f6f8 45%,#c9d2dc 100%)}

.h2{font-family:"Ubuntu",sans-serif;font-weight:300;font-size:28px}
.ideas-h{left:50px;top:774px;color:var(--teal)}
.ideas-body{left:50px;top:828px;width:496px;font-size:12.4px;line-height:19.2px}
.checklist{list-style:none;position:absolute;font-size:13px;font-weight:700;color:var(--teal)}
.checklist li{height:26.4px;padding-left:16px;position:relative}
.checklist li::before{content:"";position:absolute;left:0;top:6px;width:5px;height:5px;background:var(--yellow)}

.testi-h{left:592px;top:774px;color:var(--yellow)}
.testi-body{left:592px;top:828px;width:302px;font-size:12.4px;line-height:19px;color:var(--cyan-text)}
.byline{left:592px;top:916px;font-size:13px;font-weight:700;color:var(--grey)}
.more-btn{left:589px;top:944px;width:224px;height:34px;background:linear-gradient(#ffd83a,#f0b800);clip-path:polygon(0 0,88% 0,100% 100%,0 100%);font-family:"Ubuntu",sans-serif;font-size:20px;color:#1a1400;line-height:34px;padding-left:12px}
.more-btn b{font-weight:500;margin-left:6px}
.help-icon{left:590px;top:1007px}
.help-text{left:646px;top:1002px;font-family:"Ubuntu",sans-serif;font-weight:300;font-size:24px;color:var(--blue-light)}
.help-phone{left:642px;top:1033px;font-family:"Noto Serif",serif;font-size:24px;color:var(--cyan-text)}

.newsletter{left:913px;top:771px;width:238px;height:181px;background:linear-gradient(#1a86cf,#0c5ea8);border:1px solid #3a9ee0}
.newsletter-h{height:48px;background:linear-gradient(#eaf3f9,#b8d4e8);font-family:"Ubuntu",sans-serif;font-size:23px;color:#08203e;line-height:48px;padding-left:11px}
.field{position:absolute;left:13px;width:213px;height:27px;background:var(--white);border:1px solid #8aa;font-size:12px;color:#9aa3ad;line-height:25px;padding-left:6px}
.submit{position:absolute;left:13px;top:126px;width:108px;height:40px;background:linear-gradient(#123f80,#061f48);border:1px solid #5aa0e0;font-family:"Roboto Condensed",sans-serif;font-size:19px;line-height:38px;padding-left:11px}
.follow{left:913px;top:963px;width:238px;height:35px;background:linear-gradient(#1f7fd4,#0b4c9c);border:1px solid #3a9ee0;text-align:center;font-family:"Roboto Condensed",sans-serif;font-size:18px;line-height:33px}
.social{top:1009px;width:32px;height:32px;border-radius:50%;border:2px solid #9bd3f0}

.footer{left:24px;top:1105px;width:1150px;height:47px;background:linear-gradient(#2a82d6,#0a4790);clip-path:polygon(0 0,100% 0,97.5% 100%,2.5% 100%);border-top:1px solid #c23a3a;text-align:center;font-size:12.5px;line-height:47px;color:var(--white)}
.footer span{margin:0 8px}
</style>
</head>
<body>
<div class="backdrop"></div>

<div class="abs brand"><span class="brand-mark"></span><span class="brand-name">bRevik</span></div>
<div class="abs tagline">Your Business Capital Partners</div>

<div class="abs account"><span>Sign In</span><span>|</span><span>Sign up</span></div>

<nav class="abs nav">
  <a>Home</a><a>About Us</a><a>Services</a><a>Our Team</a><a>Testimonial</a><a style="border-right:none;box-shadow:none">Contact Us</a>
</nav>
<div class="abs search"></div>
<div class="abs search-btn">
  <svg width="54" height="24" viewBox="0 0 54 24"><circle cx="26" cy="10" r="5.5" fill="none" stroke="#111" stroke-width="2"/><line x1="22" y1="14" x2="17" y2="20" stroke="#111" stroke-width="3"/></svg>
</div>

<aside class="abs services">
  <ul><li>Strategies</li><li>Planning</li><li>Development</li><li>Solutions</li><li>Capital Raising</li></ul>
</aside>
<div class="abs services-tab"><span>OUR SERVICES</span></div>

<div class="abs hero">
  <div class="hero-photo" role="img" aria-label="Business people on phones in front of a city skyline with a globe graphic"></div>
  <div class="hero-caption"></div>
</div>
<div class="abs dots"><i></i><i class="on"></i><i></i><i></i><i></i><i></i></div>

<h1 class="abs welcome">welcome to <em>brevik,</em> your business capital partner</h1>
<div class="abs rule" style="left:50px;top:513px;width:1102px"></div>

<p class="abs intro-lead">Fusce euismod consequat ante. Lorem ipsum dolor sit met, consectetuer adipiscing elit. Pellentesque sed dolo.</p>
<p class="abs body-copy" style="left:50px;top:594px;width:625px">Aliquam congue fermentum nisl. Mauris accumsan nulla vel diam. Sed in lacus ut enim adipiscing aliquet. Nulla venenatis. In pede mi, aliquet sit amet, euismod in, auctor ut, ligula. Aliquam dapibus tincidunt metus. Praesent justo dolor, lobortis quis, lobortis dignissim, pulvinar ac, lorem. Vestibulum sed ante. Donec sagittis euismod purus.Lorem ipsum dolor sit amet, consectetuer adipiscing elit. Praesent vestibulum mo lestie</p>
<a class="abs read-more">read more</a>
<div class="abs intro-photo" role="img" aria-label="Team meeting around a laptop in a bright office"></div>

<h2 class="abs h2 ideas-h">Your Business needs fresh ideas</h2>
<div class="abs rule" style="left:50px;top:818px;width:496px"></div>
<p class="abs body-copy ideas-body">Lorem ipsum dolor sit amet, consec tetuer adipiscing elit. Praesent vestibulum molestie lacus. Aenean nonummum sociis natoque penatibus et magnis Nulla dui. Fusce feugiat malesuada odio. Morbi nunc odio, gravida at, cursus nec, luctus a, lorem. Maecenas tristique orci ac sem. Duis ultricies pharetra magna. Donec accumsan malesuada orci. Donec sit amet eros. Lorem ipsum dolor sit amet, consectetuer adipiscing elit.</p>
<ul class="checklist" style="left:57px;top:956px">
  <li>Management Consulting</li><li>Policy and Regulatory Analysis</li><li>Market Assessment</li><li>Program Management</li>
</ul>
<ul class="checklist" style="left:312px;top:956px">
  <li>Scientific and Risk Assessment</li><li>Change Management</li><li>Information Technology</li><li>Strategic Communications</li>
</ul>

<h2 class="abs h2 testi-h">Testimonials</h2>
<div class="abs rule" style="left:592px;top:818px;width:300px"></div>
<p class="abs testi-body">Lorem ipsum dolor sit amet, consec tetuer adipiscing elit. Praesent vestibulum molestie lacus. Aenean nonummum sociis natoque penatibus et magnis Nulla dui. Fusce feugiat malesuada odio. Morbi nunc odio,</p>
<p class="abs byline">By Tom Ardley, CEO Lumora Studio</p>
<div class="abs more-btn">More Testimonials <b>»</b></div>

<svg class="abs help-icon" width="42" height="42" viewBox="0 0 42 42">
  <circle cx="21" cy="21" r="20" fill="#2a8fd8" stroke="#bfe3f7" stroke-width="2"/>
  <path d="M15 11c-2 1-3 3-2 6 2 6 6 11 12 14 3 1 5 0 6-2l-4-4-3 2c-3-2-5-4-7-7l2-3z" fill="#ffffff"/>
</svg>
<div class="abs help-text">For Any Help Call Us</div>
<div class="abs help-phone">888.3147.5920</div>

<section class="abs newsletter">
  <div class="newsletter-h">Subscribe Newsletter</div>
  <div class="field" style="top:56px">Your Name</div>
  <div class="field" style="top:91px">Youe Email Id</div>
  <div class="submit">SUBMIT ›</div>
</section>
<div class="abs follow">FOLLOW US ON</div>
<span class="abs social" style="left:932px;background:#1f5fb0" aria-label="Social profile"></span>
<span class="abs social" style="left:988px;background:#3fb0e8" aria-label="Social profile"></span>
<span class="abs social" style="left:1044px;background:#f07a1a" aria-label="Feed"></span>
<span class="abs social" style="left:1099px;background:#1d8fc8" aria-label="Social profile"></span>

<footer class="abs footer">
  <span>© 2011, All Rights Reserved, brevik.com</span>|<span>Privacy Policy</span>|<span>Terms &amp; Conditions</span>
</footer>
</body>
</html>
```